Shopify website design for clothing brand.

We need a website design for our clothing brand. We are looking for a colourful and fun design to fit into the brand concept.

```html
<!DOCTYPE html>
<html lang="en">
<head>
<meta charset="utf-8">
<title>Brightstitch — Clothing</title>
<link rel="stylesheet" href="https://fonts.googleapis.com/css2?family=Federo&family=Noto+Sans:wght@400;500;600&display=swap">
<style>
:root{
  --plum:#6e1249;
  --sun:#fbe61e;
  --cream:#fdf6c3;
  --lilac:#e2d0de;
  --ink:#222222;
  --muted:#555555;
  --card:#f4f4f4;
  --footer:#2b2b2b;
  --footer-text:#d8d8d8;
  --white:#ffffff;
}
*{box-sizing:border-box;margin:0;padding:0}
html,body{width:1200px;height:3578px;overflow:hidden}
body{position:relative;font-family:"Noto Sans",sans-serif;color:var(--ink);background:var(--white)}
a{text-decoration:none}
.abs{position:absolute}
.display{font-family:"Federo",sans-serif;font-weight:400}

.promo-bar{left:0;top:0;width:1200px;height:33px;background:var(--plum);color:var(--white);font-size:13px;display:flex;align-items:center;justify-content:center}

.site-header{left:0;top:33px;width:1200px;height:72px;background:var(--white)}
.brand-name{left:122px;top:16px;font-weight:600;font-size:30px;color:var(--plum);letter-spacing:1px;display:flex;align-items:center;gap:10px}
.brand-name .dot{width:14px;height:14px;border-radius:50%;background:var(--sun)}
.main-nav{top:24px;font-size:16px;color:var(--ink)}
.main-nav.active::after{content:"";position:absolute;left:0;right:0;top:46px;height:2px;background:var(--plum)}
.header-icon{top:25px}

.hero{left:0;top:105px;width:1200px;height:455px;background:linear-gradient(100deg,#c9a58e 0%,#b66a64 40%,#a8395a 70%,#7e3a3a 100%)}
.hero-title{left:0;width:1200px;top:380px;text-align:center;font-size:52px;color:var(--white);letter-spacing:1px}

.btn{display:flex;align-items:center;justify-content:center;gap:12px;border-radius:24px;font-size:16px;font-weight:500}
.btn-sun{background:var(--sun);color:var(--plum)}
.btn-plum{background:var(--plum);color:var(--white)}

.feature{top:579px;height:116px;display:flex;flex-direction:column;align-items:center;justify-content:center;gap:10px;font-size:16px;color:var(--ink)}

.section-title{left:0;width:1200px;text-align:center;font-size:46px;color:var(--ink)}

.collection-card{top:813px;height:387px}
.collection-label{position:absolute;left:33px;bottom:31px;color:var(--white);font-size:16px;font-weight:500;display:flex;align-items:center;gap:14px}

.product-image{width:225px;height:243px;border-radius:8px}
.sale-badge{position:absolute;right:12px;top:11px;background:var(--plum);color:var(--white);font-size:10px;padding:2px 8px;border-radius:9px}
.product-info{width:225px;text-align:center}
.product-name{font-size:18px;color:var(--ink)}
.product-desc{font-size:14px;color:var(--muted);margin-top:9px}
.product-price{font-size:14px;color:var(--ink);margin-top:11px}

.story-panel{left:0;top:2341px;width:629px;height:434px;background:var(--plum);color:var(--white)}
.story-title{left:111px;top:94px;font-size:46px}
.story-text{left:111px;top:175px;width:500px;font-size:15.5px;line-height:39px}

.banner{top:2806px;height:319px;display:flex;align-items:center;justify-content:center}
.banner-title{font-size:36px;color:var(--white);letter-spacing:1px}

.site-footer{left:0;top:3146px;width:1200px;height:432px;background:var(--footer);color:var(--footer-text)}
.footer-brand{left:113px;top:62px;font-size:30px;font-weight:600;color:var(--sun);letter-spacing:1px}
.footer-about{left:113px;top:122px;width:390px;font-size:15px;line-height:28px}
.footer-heading{font-size:16px;font-weight:600;color:var(--white)}
.footer-link{font-size:15px;display:flex;align-items:center;gap:10px}
.footer-label{font-size:16px;font-weight:600;color:var(--white)}
.footer-value{font-size:15px;line-height:26px}
.payments{left:403px;top:364px;display:flex;gap:6px}
.payments span{width:32px;height:20px;border-radius:3px;background:#e9e9e9}
.copyright{left:0;width:1200px;top:402px;text-align:center;font-size:13px;color:#aaaaaa}
</style>
</head>
<body>

<div class="abs promo-bar">Seasonal sale! Save 10% on all sweaters. Free shipping for all orders over $$$.</div>

<header class="abs site-header">
  <div class="abs brand-name"><span class="dot"></span>BRIGHTSTITCH</div>
  <nav>
    <span class="abs main-nav active" style="left:657px">Home</span>
    <span class="abs main-nav" style="left:733px">Shop
      <svg width="10" height="8" viewBox="0 0 10 8"><path d="M1 2l4 4 4-4" fill="none" stroke="#222" stroke-width="1.3"/></svg></span>
    <span class="abs main-nav" style="left:817px">News</span>
    <span class="abs main-nav" style="left:890px">Contact Us</span>
  </nav>
  <svg class="abs header-icon" style="left:1012px" width="20" height="22" viewBox="0 0 20 22"><circle cx="10" cy="6.5" r="4.5" fill="none" stroke="#222" stroke-width="1.5"/><path d="M2 21c0-5 3.5-7.5 8-7.5s8 2.5 8 7.5" fill="none" stroke="#222" stroke-width="1.5"/></svg>
  <svg class="abs header-icon" style="left:1050px" width="22" height="22" viewBox="0 0 22 22"><path d="M1 2h3l2.5 12h11l2-9H6" fill="none" stroke="#222" stroke-width="1.5" stroke-linejoin="round"/><circle cx="8" cy="18.5" r="1.6" fill="#222"/><circle cx="16" cy="18.5" r="1.6" fill="#222"/></svg>
</header>

<section class="abs hero" role="img" aria-label="Photo of a woman in a red outfit seated in a rattan chair beside a potted plant"></section>
<h1 class="abs hero-title display">So many ways to express yourself</h1>
<a class="abs btn btn-sun" style="left:529px;top:467px;width:142px;height:44px">Shop Now
  <svg width="14" height="12" viewBox="0 0 14 12"><path d="M1 6h11M7.5 1.5L12 6l-4.5 4.5" fill="none" stroke="currentColor" stroke-width="1.6"/></svg></a>

<div class="abs feature" style="left:0;width:386px;background:var(--cream)">
  <svg width="28" height="32" viewBox="0 0 28 32"><path d="M14 2a9 9 0 0 0-9 9c0 7 9 15 9 15s9-8 9-15a9 9 0 0 0-9-9z" fill="none" stroke="#111" stroke-width="2.5"/><circle cx="14" cy="11" r="3.2" fill="#111"/><ellipse cx="14" cy="29" rx="9" ry="2" fill="none" stroke="#111" stroke-width="2"/></svg>
  <span>Locally Owned</span>
</div>
<div class="abs feature" style="left:407px;width:386px;background:var(--lilac)">
  <svg width="48" height="30" viewBox="0 0 48 30"><rect x="8" y="2" width="24" height="18" rx="2" fill="#111"/><path d="M32 8h8l6 7v7H32z" fill="#111"/><rect x="0" y="6" width="6" height="2" fill="#111"/><rect x="2" y="11" width="5" height="2" fill="#111"/><circle cx="15" cy="24" r="4" fill="#111" stroke="#e2d0de" stroke-width="2"/><circle cx="38" cy="24" r="4" fill="#111" stroke="#e2d0de" stroke-width="2"/></svg>
  <span>Fast Shipping</span>
</div>
<div class="abs feature" style="left:814px;width:386px;background:var(--cream)">
  <svg width="30" height="32" viewBox="0 0 30 32"><circle cx="15" cy="12" r="10" fill="none" stroke="#111" stroke-width="2.5"/><path d="M10 12l3.5 3.5L20 9" fill="none" stroke="#111" stroke-width="2.5"/><path d="M8 19l-4 10 5-2 3 4 3-9M22 19l4 10-5-2-3 4-3-9" fill="#111"/></svg>
  <span>365 Day Guarantee</span>
</div>

<h2 class="abs section-title display" style="top:722px">Collection list</h2>

<a class="abs collection-card" style="left:0;width:288px;background:linear-gradient(160deg,#3f5a34,#8a8670 60%,#c4b9a6)" role="img" aria-label="Photo of a woman in sunglasses and a light top against greenery">
  <span class="collection-label">Graphic Tees <svg width="14" height="12" viewBox="0 0 14 12"><path d="M1 6h11M7.5 1.5L12 6l-4.5 4.5" fill="none" stroke="#fff" stroke-width="1.6"/></svg></span></a>
<a class="abs collection-card" style="left:304px;width:288px;background:linear-gradient(160deg,#a5a5a3,#55605e 55%,#1f4848)" role="img" aria-label="Photo of a man in a teal hoodie on a grey backdrop">
  <span class="collection-label">Men's <svg width="14" height="12" viewBox="0 0 14 12"><path d="M1 6h11M7.5 1.5L12 6l-4.5 4.5" fill="none" stroke="#fff" stroke-width="1.6"/></svg></span></a>
<a class="abs collection-card" style="left:608px;width:288px;background:linear-gradient(165deg,#2f5f7a,#7d8e95 45%,#c0623a 70%,#5b6a74)" role="img" aria-label="Photo of a woman in an orange jacket and sunglasses under a blue sky">
  <span class="collection-label">Women's <svg width="14" height="12" viewBox="0 0 14 12"><path d="M1 6h11M7.5 1.5L12 6l-4.5 4.5" fill="none" stroke="#fff" stroke-width="1.6"/></svg></span></a>
<a class="abs collection-card" style="left:913px;width:287px;background:linear-gradient(160deg,#d4c7b4,#a08a74 50%,#3d3a3a 80%,#8a6b4f)" role="img" aria-label="Photo of a man in a checked blazer seated on stone steps">
  <span class="collection-label">Apparel <svg width="14" height="12" viewBox="0 0 14 12"><path d="M1 6h11M7.5 1.5L12 6l-4.5 4.5" fill="none" stroke="#fff" stroke-width="1.6"/></svg></span></a>

<a class="abs btn btn-plum" style="left:514px;top:1239px;width:172px;height:47px">All Collection
  <svg width="14" height="12" viewBox="0 0 14 12"><path d="M1 6h11M7.5 1.5L12 6l-4.5 4.5" fill="none" stroke="currentColor" stroke-width="1.6"/></svg></a>

<h2 class="abs section-title display" style="top:1348px">Our Featured</h2>

<div class="abs product-image" style="left:113px;top:1439px;background:radial-gradient(ellipse at center,#a3a88a 0%,#d4d6cb 45%,var(--card) 75%)" role="img" aria-label="Product photo of an olive green hoodie"><span class="sale-badge">On Sale</span></div>
<div class="abs product-image" style="left:361px;top:1439px;background:radial-gradient(ellipse at center,#8a8a8a 0%,#d2d2d2 45%,var(--card) 75%)" role="img" aria-label="Product photo of a black trucker cap with mesh back"></div>
<div class="abs product-image" style="left:613px;top:1439px;background:radial-gradient(ellipse at center,#b4b4b4 0%,#dadada 45%,var(--card) 75%)" role="img" aria-label="Product photo of a grey crew neck t-shirt"></div>
<div class="abs product-image" style="left:864px;top:1439px;background:radial-gradient(ellipse at center,#6a6a6a 0%,#cdcdcd 45%,var(--card) 75%)" role="img" aria-label="Product photo of a black t-shirt"></div>

<div class="abs product-info" style="left:113px;top:1703px"><div class="product-name">Lorem ipsum</div><div class="product-desc">Neque porro quisquam est</div><div class="product-price">$8.99</div></div>
<div class="abs product-info" style="left:361px;top:1703px"><div class="product-name">Lorem ipsum</div><div class="product-desc">Neque porro quisquam est</div><div class="product-price">$8.99</div></div>
<div class="abs product-info" style="left:613px;top:1703px"><div class="product-name">Lorem ipsum</div><div class="product-desc">Neque porro quisquam est</div><div class="product-price">$8.99</div></div>
<div class="abs product-info" style="left:864px;top:1703px"><div class="product-name">Lorem ipsum</div><div class="product-desc">Neque porro quisquam est</div><div class="product-price">$8.99</div></div>

<div class="abs product-image" style="left:113px;top:1834px;background:radial-gradient(ellipse at center,#f2bcb6 0%,#f1dcd9 45%,var(--card) 75%)" role="img" aria-label="Product photo of a pink hoodie"><span class="sale-badge">On Sale</span></div>
<div class="abs product-image" style="left:361px;top:1834px;background:radial-gradient(ellipse at center,#dcdcdc 0%,#e9e9e9 45%,var(--card) 75%)" role="img" aria-label="Product photo of a white bucket hat"></div>
<div class="abs product-image" style="left:613px;top:1834px;background:radial-gradient(ellipse at center,#a6a6a6 0%,#d6d6d6 45%,var(--card) 75%)" role="img" aria-label="Product photo of a grey t-shirt"><span class="sale-badge">On Sale</span></div>
<div class="abs product-image" style="left:864px;top:1834px;background:radial-gradient(ellipse at center,#dadc9c 0%,#e8e9cd 45%,var(--card) 75%)" role="img" aria-label="Product photo of a pale lime sweatshirt"></div>

<div class="abs product-info" style="left:113px;top:2098px"><div class="product-name">Lorem ipsum</div><div class="product-desc">Neque porro quisquam est</div><div class="product-price">$8.99</div></div>
<div class="abs product-info" style="left:361px;top:2098px"><div class="product-name">Lorem ipsum</div><div class="product-desc">Neque porro quisquam est</div><div class="product-price">$8.99</div></div>
<div class="abs product-info" style="left:613px;top:2098px"><div class="product-name">Lorem ipsum</div><div class="product-desc">Neque porro quisquam est</div><div class="product-price">$8.99</div></div>
<div class="abs product-info" style="left:864px;top:2098px"><div class="product-name">Lorem ipsum</div><div class="product-desc">Neque porro quisquam est</div><div class="product-price">$8.99</div></div>

<a class="abs btn btn-sun" style="left:485px;top:2227px;width:229px;height:47px">Shop this collection
  <svg width="14" height="12" viewBox="0 0 14 12"><path d="M1 6h11M7.5 1.5L12 6l-4.5 4.5" fill="none" stroke="currentColor" stroke-width="1.6"/></svg></a>

<section class="abs story-panel">
  <h2 class="abs story-title display">Our Story</h2>
  <p class="abs story-text">Duis aute irure dolor in reprehenderit in voluptate velit esse cillum dolore eu fugiat nulla pariatur. Excepteur sint occaecat cupidatat.</p>
  <a class="abs btn btn-sun" style="left:111px;top:293px;width:175px;height:46px">Learn More
    <svg width="14" height="12" viewBox="0 0 14 12"><path d="M1 6h11M7.5 1.5L12 6l-4.5 4.5" fill="none" stroke="currentColor" stroke-width="1.6"/></svg></a>
</section>
<div class="abs" style="left:629px;top:2341px;width:571px;height:434px;background:linear-gradient(120deg,#6b5a3a,#c9a27c 35%,#e8c9a8 55%,#4f6048 85%,#2f3f30)" role="img" aria-label="Photo of a smiling group of five friends outdoors"></div>

<div class="abs banner" style="left:0;width:588px;background:linear-gradient(135deg,#c9c6c2,#e08a32 45%,#d9d6d2 75%)" role="img" aria-label="Photo of a woman in an orange hoodie and sunglasses">
  <span class="banner-title display">Planet-friendly garments</span></div>
<div class="abs banner" style="left:613px;width:587px;background:linear-gradient(135deg,#cfcccb,#b88a64 50%,#d8d4d1 80%)" role="img" aria-label="Photo of a woman in a knit sweater seated on the floor">
  <span class="banner-title display">Our clothes are made to last</span></div>

<footer class="abs site-footer">
  <div class="abs footer-brand">BRIGHTSTITCH</div>
  <p class="abs footer-about">Lorem ipsum dolor sit amet, consectetur adipiscing elit, sed do eiusmod tempor incididunt ut labore et dolore magna aliqua. facilisis.</p>
  <div class="abs" style="left:113px;top:230px"><div class="footer-label">Address</div><div class="footer-value">Brightstitch,<br>Address comes here.</div></div>
  <div class="abs" style="left:309px;top:230px"><div class="footer-label">Phone</div><div class="footer-value">+1 555-010-0199</div>
    <div class="footer-label" style="margin-top:6px">Email</div><div class="footer-value">hello@brightstitch.example</div></div>

  <div class="abs footer-heading" style="left:567px;top:68px">Shop Brightstitch</div>
  <div class="abs footer-link" style="left:567px;top:122px">Search</div>
  <div class="abs footer-link" style="left:567px;top:157px">Shop All</div>
  <div class="abs footer-link" style="left:567px;top:191px">About Us</div>
  <div class="abs footer-link" style="left:567px;top:225px">Contact Us</div>

  <div class="abs footer-heading" style="left:764px;top:68px">Customer Services</div>
  <div class="abs footer-link" style="left:764px;top:122px">Contact Us</div>
  <div class="abs footer-link" style="left:764px;top:157px">Terms &amp; Conditions</div>
  <div class="abs footer-link" style="left:764px;top:191px">Privacy Policy</div>

  <div class="abs footer-heading" style="left:953px;top:68px">Follow Us</div>
  <div class="abs footer-link" style="left:953px;top:123px"><svg width="10" height="10"><circle cx="5" cy="5" r="4" fill="#d8d8d8"/></svg>Community</div>
  <div class="abs footer-link" style="left:953px;top:158px"><svg width="10" height="10"><circle cx="5" cy="5" r="4" fill="#d8d8d8"/></svg>Updates</div>
  <div class="abs footer-link" style="left:953px;top:193px"><svg width="10" height="10"><circle cx="5" cy="5" r="4" fill="#d8d8d8"/></svg>Moodboard</div>
  <div class="abs footer-link" style="left:953px;top:227px"><svg width="10" height="10"><circle cx="5" cy="5" r="4" fill="#d8d8d8"/></svg>Gallery</div>

  <div class="abs payments" aria-label="Accepted payment methods">
    <span></span><span></span><span></span><span></span><span></span><span></span><span></span><span></span><span></span><span></span><span></span>
  </div>
  <div class="abs copyright">2023 Brightstitch. All Rights Reserved.</div>
</footer>

</body>
</html>
```